Velmora Investment Management Needs Door Wording Design

We need someone to put together a design for our glass front doors (2).

The words could be, but aren't limited to, as follows:

"100
Serenely Restorative Bodywork
*Ring Bell"

and

"200 & 300
Velmora Investment Management inc.
*Ring Bell"

The design should be clean, subtle and professional. It is a simple mainly glass door with a black frame. Our website is www.velmorainvest.ca for a more detailed description of what we do. The adjacent business would also be involved, as per the wording of the Serenely Restorative Bodywork.

We are looking for something to bring out the wording on the door (there is currently a piece of paper printed and taped to the inside).

Dimensions of the window are 47 inches x 23 inches.

Thanks!

Colors
000000
ffffff

Requirements
Must have
• The previous words
Nice to have
• Creative flair, taking into consideration the nature of our business (Investment Management)

```html
<!DOCTYPE html>
<html lang="en">
<head>
<meta charset="utf-8">
<title>Suite 100 Door Lettering</title>
<link rel="stylesheet" href="https://fonts.googleapis.com/css2?family=Oswald:wght@400&family=Montserrat:wght@500&display=swap">
<style>
  :root {
    --glass: #0e0e0e;
    --vinyl: #f4f4f4;
  }
  html, body {
    margin: 0;
    padding: 0;
    width: 1200px;
    height: 1021px;
    overflow: hidden;
    background: var(--glass);
  }
  .door-lettering {
    position: relative;
    width: 1200px;
    height: 1021px;
    background: var(--glass);
    color: var(--vinyl);
  }
  .suite-number {
    position: absolute;
    top: 82px;
    left: 0;
    width: 1214px;
    margin: 0;
    text-align: center;
    font-family: "Oswald", "Arial Narrow", sans-serif;
    font-weight: 400;
    font-size: 224px;
    line-height: 1;
    letter-spacing: 2px;
  }
  .divider {
    position: absolute;
    left: 522px;
    width: 177px;
    height: 2px;
    background: var(--vinyl);
  }
  .divider--top { top: 417px; }
  .divider--bottom { top: 754px; }
  .business-name {
    position: absolute;
    top: 458px;
    left: 0;
    width: 1214px;
    margin: 0;
    text-align: center;
    font-family: "Oswald", "Arial Narrow", sans-serif;
    font-weight: 400;
    font-size: 66px;
    line-height: 77px;
    letter-spacing: 1px;
    text-transform: uppercase;
  }
  .business-name span { display: block; }
  .entry-note {
    position: absolute;
    top: 788px;
    left: 0;
    width: 1222px;
    margin: 0;
    text-align: center;
    font-family: "Montserrat", "Helvetica Neue", sans-serif;
    font-weight: 500;
    font-size: 23px;
    letter-spacing: 3px;
    text-transform: uppercase;
  }
</style>
</head>
<body>
  <main class="door-lettering">
    <p class="suite-number">100</p>
    <div class="divider divider--top"></div>
    <h1 class="business-name">
      <span>Serenely</span>
      <span>Restorative</span>
      <span>Bodywork</span>
    </h1>
    <div class="divider divider--bottom"></div>
    <p class="entry-note">Ring Bell</p>
  </main>
</body>
</html>
```